Car Detailing Brochure/PriceList

Looking for a nicely designed Brochure/Price sheet that can be displayed on the website and Chatterlane sites which details the different service stages available to potential customers

Target Market(s)

People in the local area who need paint enhancement and correction

Industry/Entity Type

Car Detailing

Requirements
Must have
• Reader Friendly, Informative, pictures (lots on Chatterlane/Website that can be used) would like to see nicely imbedded pictures relating to stages etc
Nice to have
• Luxury design following company branding with logo/colours etc https://www.thecorvalestudio.uk/services

```html
<!DOCTYPE html>
<html lang="en">
<head>
<meta charset="utf-8">
<title>Corvale Studio – Price List</title>
<link rel="stylesheet" href="https://fonts.googleapis.com/css2?family=Oswald:wght@400;500;600;700&family=Lato:wght@400;700;900&display=swap">
<style>
  :root{
    --bg:#6d6c75;
    --ink:#0b0b0b;
    --white:#ffffff;
    --paper:#e9e9e9;
    --grey-bar:#3a3a3a;
    --orange-1:#e0953f;
    --orange-2:#c7672a;
    --orange-3:#b74a22;
    --accent:#e07a2c;
    --header-dark:#3a1606;
    --header-glow:#a8481a;
    --title-grey:#d9d9d9;
  }
  *{box-sizing:border-box;margin:0;padding:0}
  html,body{width:1200px;height:1200px;overflow:hidden;background:var(--bg)}
  body{position:relative;font-family:"Lato",sans-serif}
  .flyer{
    position:absolute;left:197px;top:30px;width:697px;height:986px;
    transform:scale(1.156);transform-origin:0 0;
    background:var(--ink);overflow:hidden;
    box-shadow:0 4px 14px rgba(0,0,0,.35);
  }
  .abs{position:absolute}
  .top-white{left:0;top:0;width:697px;height:190px;background:var(--white)}
  .header-band{left:0;top:0;width:697px;height:200px}
  .price-title{left:20px;top:16px;font-family:"Oswald",sans-serif;font-weight:700;line-height:.86;text-transform:uppercase}
  .price-title .l1{font-size:74px;letter-spacing:1px;display:block;color:#9a9a9a}
  .price-title .l2{font-size:100px;display:block;color:#141414}
  .brand{left:262px;top:74px;width:400px;text-align:center;font-family:"Oswald",sans-serif;font-weight:600;font-size:44px;color:var(--white);letter-spacing:.5px;line-height:1}
  .tagline{left:262px;top:130px;width:400px;text-align:center;font-family:"Oswald",sans-serif;font-weight:500;font-size:19px;color:var(--white);letter-spacing:.3px;white-space:nowrap}

  .stage-title{font-family:"Oswald",sans-serif;font-weight:600;font-size:38px;color:var(--title-grey);line-height:1}
  .stage-title span{color:var(--accent)}
  .col{position:absolute;width:205px;display:flex;flex-direction:column}
  .col .intro{background:var(--paper);color:var(--tone);font-weight:700;font-size:11.5px;text-align:center;text-transform:uppercase;padding:7px 8px 8px;line-height:1.3;border-top:4px solid var(--tone)}
  .col .body{flex:1;background:var(--tone);color:var(--white);font-size:11.4px;line-height:1.3;padding:10px 8px 6px}
  .col .body p+p{margin-top:8px}
  .col .ticks{list-style:none;margin-top:12px;font-size:10.6px;font-weight:700;text-transform:uppercase;line-height:1.25}
  .col .protect{background:var(--paper);color:var(--accent);font-size:10.8px;font-weight:700;text-align:center;padding:3px 0;text-transform:uppercase}
  .col .days{background:var(--grey-bar);color:var(--white);font-size:10.8px;font-weight:700;text-align:center;padding:3px 0;text-transform:uppercase}
  .col .prices{background:var(--white);height:78px;display:flex;align-items:center;padding:0 6px;gap:8px}
  .coin{width:60px;height:60px;flex:none;border-radius:50%;border:3px solid var(--tone);display:flex;align-items:center;justify-content:center}
  .coin b{width:46px;height:46px;border-radius:50%;background:var(--tone);color:var(--white);display:flex;align-items:center;justify-content:center;font-family:"Oswald",sans-serif;font-size:30px;font-weight:500}
  .prices ul{list-style:none;font-size:10.6px;font-weight:900;color:#111;text-transform:uppercase;line-height:1.3}
  .prices li::before{content:"▸ ";color:var(--accent);font-size:9px}
  .prices li em{font-style:normal;font-weight:700;color:var(--accent)}
  .col .note{background:var(--tone);color:var(--white);font-size:10.4px;line-height:1.2;padding:4px 8px 6px;height:45px}
  .stage-1{--tone:var(--orange-1)}
  .stage-2{--tone:var(--orange-2)}
  .stage-3{--tone:var(--orange-3)}
  .popular{background:var(--orange-2);color:var(--white);font-family:"Oswald",sans-serif;font-weight:500;font-size:18px;border-radius:6px;padding:1px 0 2px;margin:0 0 6px;text-transform:uppercase}

  .upgrades-head{left:445px;top:782px;width:252px;height:36px;background:var(--orange-2);color:var(--white);font-family:"Oswald",sans-serif;font-size:15px;font-weight:500;display:flex;align-items:center;justify-content:flex-end;padding-right:20px;text-transform:uppercase;white-space:nowrap}
  .upgrades{left:395px;top:818px;width:302px;height:118px;background:var(--white);clip-path:polygon(16% 0,100% 0,100% 100%,0 100%)}
  .upgrades ul{list-style:none;position:absolute;right:16px;top:9px;width:255px;text-align:right;font-size:9.3px;line-height:1.3;color:#111}
  .upgrades li::before{content:"• ";color:var(--accent)}
  .upgrades li.cont::before{content:""}
  .upgrades b{font-weight:900}
  .upgrades em{font-style:normal;color:var(--accent)}
  .contact{left:390px;top:944px;width:307px;height:42px;background:var(--orange-1);clip-path:polygon(9% 0,100% 0,100% 100%,0 100%);display:flex;align-items:center;justify-content:flex-end;gap:8px;padding-right:18px;font-family:"Oswald",sans-serif;color:var(--white);font-size:22px;font-weight:500;letter-spacing:.5px;white-space:nowrap}
  .contact span{flex:none}
  .contact .phone{width:30px;height:30px;border-radius:50%;border:2px solid var(--white);display:flex;align-items:center;justify-content:center}
</style>
</head>
<body>
<main class="flyer">
  <div class="abs top-white"></div>
  <svg class="abs header-band" viewBox="0 0 697 200" width="697" height="200" aria-hidden="true">
    <defs>
      <radialGradient id="glow" cx="62%" cy="20%" r="70%">
        <stop offset="0" stop-color="#a8481a"/>
        <stop offset="1" stop-color="#3a1606"/>
      </radialGradient>
    </defs>
    <polygon points="182,0 697,0 697,178 252,178" fill="url(#glow)"/>
    <polygon points="0,190 440,190 430,200 0,200" fill="#c7672a"/>
    <polygon points="440,190 665,190 660,198 436,198" fill="#5a2a10"/>
    <polygon points="665,182 697,178 697,200 655,200" fill="#0b0b0b"/>
  </svg>
  <svg class="abs" style="left:0;top:205px" width="697" height="20" aria-hidden="true">
    <polygon points="0,4 228,4 220,14 0,14" fill="#e0953f"/>
  </svg>

  <h1 class="abs price-title"><span class="l1">Price</span><span class="l2">List</span></h1>
  <div class="abs brand">CORVALESTUDIO.UK</div>
  <div class="abs tagline">DETAILING, PAINT CORRECTION AND ENHANCEMENT</div>

  <h2 class="abs stage-title" style="left:32px;top:272px">STAGE <span>1</span></h2>
  <h2 class="abs stage-title" style="left:248px;top:244px">STAGE <span>2</span></h2>
  <h2 class="abs stage-title" style="left:464px;top:210px">STAGE <span>3</span></h2>

  <section class="col stage-1" style="left:27px;top:318px;height:440px">
    <div class="intro">Ideally suited to brand new or exceptionally well-maintained vehicles.</div>
    <div class="body">
      <p>This Stage will remove light swirl marks, marring &amp; micro scratches typically found in new car preparation or from home car washing methods. It includes:</p>
      <ul class="ticks">
        <li>✓ Full inspection &amp; prewash</li>
        <li>✓ Wheels cleaned</li>
        <li>✓ Snow foam</li>
        <li>✓ Decontamination process</li>
        <li>✓ Single stage machine polish</li>
        <li>✓ Glass cleaned</li>
        <li>✓ A liquid wax finish.</li>
      </ul>
    </div>
    <div class="protect">Up to 6 months protection</div>
    <div class="days">Takes between 1 – 1.5 days</div>
    <div class="prices"><div class="coin"><b>$</b></div>
      <ul><li>Small car <em>£240</em></li><li>Medium car <em>£270</em></li><li>Large car <em>£300</em></li><li>4x4s/pickups/vans<br>&nbsp;&nbsp;from <em>£350</em></li></ul></div>
    <div class="note">*Upgrade to a hard wax finish with up to 12 months protection + interior valet from £130</div>
  </section>

  <section class="col stage-2" style="left:245px;top:288px;height:470px">
    <div class="intro" style="border-top:0;padding-top:6px">
      <div class="popular">★ Most Popular ★</div>
      This is our most popular package and will suit most vehicles.
    </div>
    <div class="body">
      <p>It includes everything from stage 1 plus a 2-stage polish that will address light scratches and imperfection, oxidation and begin to correct and level the paint surface resulting in an exceptional shine.</p>
      <p>Combined with a hard wax coating this will not only lock in the shine for longer but also make home cleaning and maintenance easier and more effective.</p>
    </div>
    <div class="protect">6 -9 months protection</div>
    <div class="days">Takes from 2.5 days</div>
    <div class="prices"><div class="coin"><b>$</b></div>
      <ul><li>Small car <em>£400</em></li><li>Medium car <em>£430</em></li><li>Large car <em>£460</em></li><li>4x4/pickups/vans<br>&nbsp;&nbsp;from <em>£500</em></li></ul></div>
    <div class="note">*Upgrade to a ceramic coating with 2 - 3 years protection + interior valet from £250</div>
  </section>

  <section class="col stage-3" style="left:463px;top:256px;height:502px">
    <div class="intro">This is our luxury level<br>paint correction</div>
    <div class="body">
      <p>It includes everything from stage 2 plus a 3 stage polish that will provide a glorious, better than new, mirror like shine. The 3 stage polish will remove medium to heavy scratches and will level the paint to give that wet look glossy finish you never thought possible.</p>
      <p style="margin-top:14px">For the ultimate protection we recommend taking advantage of a professional grade ceramic coating which when applied will lock in that glossy finish and provide the longest possible protection. A full valet is included on this stage and with basic hard wax</p>
    </div>
    <div class="protect">Up to 12 months protection</div>
    <div class="days">Takes from 3.5 days</div>
    <div class="prices"><div class="coin"><b>$</b></div>
      <ul><li>Small car <em>£600</em></li><li>Medium car <em>£630</em></li><li>Large car <em>£660</em></li><li>4x4/pickups/vans<br>&nbsp;&nbsp;from <em>£700</em></li></ul></div>
    <div class="note">*Interior valet included, add ceramic coating with 2 - 3 years protection from £200</div>
  </section>

  <svg class="abs" style="left:10px;top:768px" width="370" height="210" viewBox="0 0 370 210" role="img" aria-label="Diamond-framed photos of detailed cars: a white car in a studio, a red coupe, a blue hatchback and a grey saloon">
    <defs>
      <linearGradient id="ph" x1="0" y1="0" x2="1" y2="1">
        <stop offset="0" stop-color="#5b6470"/><stop offset="1" stop-color="#2a2f38"/>
      </linearGradient>
      <radialGradient id="flare" cx="30%" cy="78%" r="35%">
        <stop offset="0" stop-color="#ffffff" stop-opacity=".9"/><stop offset="1" stop-color="#ffffff" stop-opacity="0"/>
      </radialGradient>
    </defs>
    <g stroke="#ffffff" stroke-width="3">
      <polygon points="80,10 150,80 80,150 10,80" fill="#8a8e92"/>
      <polygon points="185,10 255,80 185,150 115,80" fill="#9c2c26"/>
      <polygon points="290,10 358,78 290,146 222,78" fill="#2f5fa8"/>
      <polygon points="130,70 195,135 130,200 65,135" fill="#c9cbcd"/>
      <polygon points="240,70 305,135 240,200 175,135" fill="url(#ph)"/>
    </g>
    <rect width="370" height="210" fill="url(#flare)"/>
  </svg>

  <div class="abs upgrades-head">Upgrades available on all stages</div>
  <div class="abs upgrades">
    <ul>
      <li><b>Hard Carnauba Wax Protection</b> 1 year from <em>£70</em></li>
      <li><b>Ceramic Coating</b></li>
      <li class="cont">2 -3 years paint protection from <em>£200</em></li>
      <li><b>Ceramic Wheel Protection</b> from <em>£100</em></li>
      <li><b>Ceramic Leather protection</b> from <em>£100</em></li>
      <li><b>Glass protection</b> from <em>£40</em></li>
      <li><b>Interior valet; Full deep steam clean</b> including Carpets, Mats, leather cleaner, Plastics and sanitisation from <em>£80</em></li>
    </ul>
  </div>
  <svg class="abs" style="left:388px;top:818px" width="110" height="124" aria-hidden="true">
    <polygon points="55,0 66,0 10,124 0,124" fill="#c7672a"/>
  </svg>
  <div class="abs contact">
    <span>MARCUS</span>
    <span class="phone"><svg width="16" height="16" viewBox="0 0 24 24"><path fill="#fff" d="M6.6 10.8a15.1 15.1 0 0 0 6.6 6.6l2.2-2.2a1 1 0 0 1 1-.25 11.4 11.4 0 0 0 3.6.57 1 1 0 0 1 1 1V20a1 1 0 0 1-1 1A17 17 0 0 1 3 4a1 1 0 0 1 1-1h3.5a1 1 0 0 1 1 1c0 1.25.2 2.45.57 3.57a1 1 0 0 1-.25 1z"/></svg></span>
    <span>07700 900 417</span>
  </div>
</main>
</body>
</html>
```